we are plumbers and builders.

one side with lantern installations mark fenwick 07700900417 01632960284 info@lanterninstallations.co.uk
other side
lantern construction
dean fenwick 07700900583
01632960284
info@lanternconstruction.co.uk

i don't want your bog standard logo id like something unusual maybe shape the card. i like black and silver,

```html
<!DOCTYPE html>
<html lang="en">
<head>
<meta charset="utf-8">
<title>Lantern business cards</title>
<link rel="stylesheet" href="https://fonts.googleapis.com/css2?family=Raleway:wght@400;500;700&display=swap">
<style>
  :root {
    --backdrop: #e2e2e2;
    --card-dark: #2a2a2a;
    --card-light: #f4f4f4;
    --brand-red: #dd1f26;
    --brand-blue: #4472c4;
    --silver: #aaaaaa;
    --text-light: #f2f2f2;
    --text-dark: #2a2a2a;
  }
  * { box-sizing: border-box; margin: 0; padding: 0; }
  html, body {
    width: 1200px; height: 960px; overflow: hidden;
    background: var(--backdrop);
    font-family: "Raleway", Arial, sans-serif;
    font-variant-numeric: lining-nums;
  }
  .stage { position: relative; width: 1200px; height: 960px; }

  .card {
    position: absolute; left: 310px; width: 580px; height: 341px; overflow: hidden;
  }
  .card--installations {
    top: 104px; background: var(--card-dark); color: var(--text-light);
    border-radius: 0 171px 171px 0;
  }
  .card--construction {
    top: 514px; background: var(--card-light); color: var(--text-dark);
    border-radius: 171px 0 0 171px;
  }

  .brand-ring { position: absolute; width: 280px; height: 280px; }
  .card--installations .brand-ring { left: 270px; top: 30px; }
  .card--construction .brand-ring { left: 30px; top: 30px; }

  .wordmark {
    position: absolute; color: var(--brand-red); font-weight: 500; line-height: 1;
  }
  .wordmark__name { display: block; font-size: 42px; letter-spacing: 1.5px; }
  .wordmark__trade { display: block; font-size: 16px; letter-spacing: 2.6px; margin-top: 7px; }
  .card--installations .wordmark { left: 34px; top: 52px; }
  .card--construction .wordmark { right: 32px; top: 52px; text-align: right; }

  .person { position: absolute; }
  .card--installations .person { left: 35px; top: 170px; }
  .card--construction .person { right: 32px; top: 170px; text-align: right; }
  .person__name {
    color: var(--brand-red); font-weight: 700; font-size: 19px; letter-spacing: 0.3px;
  }
  .person__role { font-size: 15px; margin-top: 2px; }

  .contacts { position: absolute; list-style: none; font-size: 16px; }
  .card--installations .contacts { left: 35px; top: 231px; }
  .card--construction .contacts { right: 32px; top: 231px; }
  .contacts li { display: flex; align-items: center; gap: 5px; height: 20.5px; white-space: nowrap; }
  .card--construction .contacts li { justify-content: flex-end; }
  .contacts svg { width: 13px; height: 13px; flex: none; }
  .icon { fill: none; stroke: var(--brand-blue); stroke-width: 1.6; }
  .icon--solid { fill: var(--brand-blue); stroke: none; }
</style>
</head>
<body>
<main class="stage">

  <section class="card card--installations" aria-label="Lantern Installations card">
    <div class="wordmark">
      <span class="wordmark__name">LANTERN</span>
      <span class="wordmark__trade">INSTALLATIONS</span>
    </div>
    <div class="person">
      <p class="person__name">MARK FENWICK</p>
      <p class="person__role">Owner</p>
    </div>
    <ul class="contacts">
      <li><svg viewBox="0 0 14 14"><rect class="icon" x="3.5" y="0.8" width="7" height="12.4" rx="1.4"/></svg>07700900417</li>
      <li><svg viewBox="0 0 14 14"><path class="icon--solid" d="M3 1l2.4 2.6-1.2 1.8c.9 1.9 2.4 3.4 4.3 4.3l1.8-1.2L13 11l-1.5 2C6 12.6 1.4 8 1 2.5z"/></svg>01632960284</li>
      <li><svg viewBox="0 0 14 14"><rect class="icon" x="1" y="3" width="12" height="8.5"/><path class="icon" d="M1 3l6 5 6-5"/></svg>info@lanterninstallations.co.uk</li>
      <li><svg viewBox="0 0 14 14"><circle class="icon" cx="7" cy="7" r="5.8"/><ellipse class="icon" cx="7" cy="7" rx="2.5" ry="5.8"/><path class="icon" d="M1.2 7h11.6"/></svg>www.lanterninstallations.co.uk</li>
    </ul>
    <svg class="brand-ring" viewBox="0 0 280 280" aria-hidden="true">
      <circle cx="140" cy="140" r="125" fill="none" stroke="var(--silver)" stroke-width="20"/>
    </svg>
  </section>

  <section class="card card--construction" aria-label="Lantern Construction card">
    <svg class="brand-ring" viewBox="0 0 280 280" aria-hidden="true">
      <circle cx="140" cy="140" r="125" fill="none" stroke="var(--silver)" stroke-width="20"/>
    </svg>
    <div class="wordmark">
      <span class="wordmark__name">LANTERN</span>
      <span class="wordmark__trade">CONSTRUCTION</span>
    </div>
    <div class="person">
      <p class="person__name">DEAN FENWICK</p>
      <p class="person__role">Owner</p>
    </div>
    <ul class="contacts">
      <li>07700900583<svg viewBox="0 0 14 14"><rect class="icon" x="3.5" y="0.8" width="7" height="12.4" rx="1.4"/></svg></li>
      <li>01632960284<svg viewBox="0 0 14 14"><path class="icon--solid" d="M3 1l2.4 2.6-1.2 1.8c.9 1.9 2.4 3.4 4.3 4.3l1.8-1.2L13 11l-1.5 2C6 12.6 1.4 8 1 2.5z"/></svg></li>
      <li>info@lanternconstruction.co.uk<svg viewBox="0 0 14 14"><rect class="icon" x="1" y="3" width="12" height="8.5"/><path class="icon" d="M1 3l6 5 6-5"/></svg></li>
      <li>www.lanternconstruction.co.uk<svg viewBox="0 0 14 14"><circle class="icon" cx="7" cy="7" r="5.8"/><ellipse class="icon" cx="7" cy="7" rx="2.5" ry="5.8"/><path class="icon" d="M1.2 7h11.6"/></svg></li>
    </ul>
  </section>

</main>
</body>
</html>
```